No Credit Score QT and ZMR

I'm looking for a banner to display on emails as well as facebook. The facebook banner would need to be square and the other size is 728 x 90. We are a mortgage company that does mostly Military home loans. We would like to start out with just this banner, then do about 20 others once we find the right designer. I need something simple but that stands out. Our company website is www.harborpeakfinancial.com. The text for this will be ( Ask about our "No Credit Score" program for ZMR and QT)

```html
<!DOCTYPE html>
<html lang="en">
<head>
<meta charset="UTF-8">
<title>No Credit Score Program Banner</title>
<link rel="stylesheet" href="https://fonts.googleapis.com/css2?family=Open+Sans:wght@600;700&display=swap">
<style>
  :root {
    --green-deep: #5e8a62;
    --green-mid: #8fb590;
    --green-light: #c3dcc0;
    --green-bright: #3fb24a;
    --brand-ink: #2f5a34;
    --cta-text: #55a548;
    --panel: #ffffff;
  }
  html, body {
    margin: 0;
    padding: 0;
    width: 1200px;
    height: 148px;
    overflow: hidden;
    background: var(--panel);
  }
  .banner {
    position: relative;
    width: 1200px;
    height: 148px;
    overflow: hidden;
    font-family: "Open Sans", Arial, sans-serif;
  }
  .banner__backdrop {
    position: absolute;
    inset: 0;
    background:
      radial-gradient(ellipse at 30% 20%, var(--green-light) 0%, transparent 60%),
      radial-gradient(ellipse at 80% 90%, var(--green-light) 0%, transparent 55%),
      linear-gradient(100deg, var(--green-deep) 0%, var(--green-mid) 45%, var(--green-light) 75%, var(--green-mid) 100%);
  }
  .banner__cta {
    position: absolute;
    left: 211px;
    top: 48px;
    width: 775px;
    height: 54px;
    box-sizing: border-box;
    padding: 0 24px;
    background: var(--panel);
    display: flex;
    align-items: center;
    justify-content: center;
    box-shadow: 0 2px 6px rgba(40, 70, 40, 0.18);
  }
  .banner__cta-text {
    margin: 0;
    color: var(--cta-text);
    font-size: 25px;
    font-weight: 600;
    line-height: 1;
    white-space: nowrap;
  }
  .brand {
    position: absolute;
    right: 0;
    top: 6px;
    width: 96px;
    display: flex;
    flex-direction: column;
    align-items: center;
    gap: 10px;
  }
  .brand__mark {
    width: 60px;
    height: 60px;
    border-radius: 10px;
    background: var(--green-bright);
  }
  .brand__name {
    color: var(--brand-ink);
    font-size: 11px;
    font-weight: 700;
    letter-spacing: 1px;
    text-transform: uppercase;
    white-space: nowrap;
  }
</style>
</head>
<body>
  <div class="banner">
    <div class="banner__backdrop" role="img" aria-label="Pattern of green suburban house rooftops"></div>
    <div class="banner__cta">
      <p class="banner__cta-text">Ask about our "No Credit Score" program for ZMR and QT</p>
    </div>
    <div class="brand">
      <div class="brand__mark"></div>
      <span class="brand__name">Harbor Peak</span>
    </div>
  </div>
</body>
</html>
```